Healthy living company needs logo / business card

We are looking for a business identity for our company that operates in the Health and Wellness area.
Our audience is those open to hearing about the links between ill health and chemicals in the home as well as how to boost their health naturally through nutrition. We show people how to eliminate those toxins and share the message with others.
We also work with and mentor people who want to build their own business, share the message and create a leveraged income.
Our business name is: Larkwell
The tag line we have is: Simple Changes ยท Healthy Living
Output for the project is:
Logo and business card design (2 people on the card).
Our perspective is for a modern, natural, simple, clean design (web 2.0 feel) that will appeal to a broad age range and audience. It should feel professional but not formal. It should not seem medical.
The logo should not be a gradient nor overly complex. Colouring should only be one or two colours at most. They can be bright, we are tending to lean towards green for obvious reasons but open to your thoughts.
Simplicity is the key.
The business card needs to be two sided. We like having the logo and card details on the front and then reversed out on the back with the logo and name in white on the colour block.
Please see the attached card brief document about the card content.

```html
<!DOCTYPE html>
<html lang="en">
<head>
<meta charset="utf-8">
<title>Larkwell — Business Card</title>
<link rel="stylesheet" href="https://fonts.googleapis.com/css2?family=Arimo:wght@400&display=swap">
<style>
  :root {
    --leaf-green: #46b549;
    --text-green: #4cb050;
    --card-white: #ffffff;
    --stage: #ecefe9;
    --dot-green: #2f7f35;
  }
  * { box-sizing: border-box; margin: 0; padding: 0; }
  html, body { width: 1200px; height: 900px; overflow: hidden; }
  body {
    background: var(--stage);
    position: relative;
    font-family: "Arimo", Arial, sans-serif;
  }
  .card {
    position: absolute;
    top: 295px;
    width: 540px;
    height: 310px;
    border-radius: 22px;
    box-shadow: 0 6px 18px rgba(0,0,0,0.12);
  }
  .card--front { left: 40px; background: var(--card-white); }
  .card--back  { left: 620px; background: var(--leaf-green); }

  .brand { position: absolute; }
  .brand__name {
    display: block;
    font-size: 40px;
    line-height: 1;
  }
  .brand__tagline {
    display: block;
    font-size: 14px;
    margin-top: 8px;
    white-space: nowrap;
  }

  .card--front .brand { left: 40px; top: 128px; color: var(--text-green); }
  .card--back .brand  { left: 40px; top: 118px; color: var(--card-white); }

  .divider {
    position: absolute;
    left: 312px;
    top: 108px;
    width: 0;
    height: 96px;
    border-left: 3px dotted var(--dot-green);
  }
  .contact {
    position: absolute;
    left: 330px;
    top: 106px;
    list-style: none;
    font-size: 11.5px;
    line-height: 16.5px;
    color: var(--text-green);
  }

  .aspirations {
    position: absolute;
    left: 300px;
    top: 50px;
    list-style: none;
    font-size: 14.5px;
    line-height: 19.8px;
    color: var(--card-white);
  }
</style>
</head>
<body>
  <section class="card card--front" aria-label="Business card front">
    <div class="brand">
      <span class="brand__name">Larkwell</span>
      <span class="brand__tagline">Everyday Wellness at Home</span>
    </div>
    <div class="divider"></div>
    <ul class="contact">
      <li>Owner Name: 000-000-0000</li>
      <li>Owner Name: 000-000-0000</li>
      <li>o: 000-000-0000</li>
      <li>e: person@livelarkwell.com</li>
      <li>web: livelarkwell.com</li>
    </ul>
  </section>

  <section class="card card--back" aria-label="Business card back">
    <div class="brand">
      <span class="brand__name">Larkwell</span>
      <span class="brand__tagline">Everyday Wellness at Home</span>
    </div>
    <ul class="aspirations">
      <li>Multiple Streams of Income</li>
      <li>Financial Freedom</li>
      <li>Own My Own Business</li>
      <li>More Time</li>
      <li>Personal Development</li>
      <li>Health and Vitality</li>
      <li>Help Others Meet New People</li>
      <li>Retirement Plan</li>
      <li>Leave a Legacy</li>
      <li>Meet New People</li>
    </ul>
  </section>
</body>
</html>
```